Cargo Van Car Wrap

We have purchased a new car and are looking for a design.

2023 Torvane 4100 Cargo Van 170"

Target Market(s)

Home Improvement - Kitchen and Bath Remodeling , Home Additions, Sunroom, Deck, Patio, Porch

Industry/Entity Type

Interior Remodeling , Home Additions . Kitchen and Bath Remodeling

Font styles to use
Sans Serif

Colors

Designer to choose colors to be used in the design.

Requirements
Must have
• Kitchen and Bathroom Pictures
Nice to have
• Office address , website, phone number and promition. 4817 Halberd Ave Silver Spring MD 20910 , www.halvorhomeworks.example - 3015550148

```html
<!DOCTYPE html>
<html lang="en">
<head>
<meta charset="utf-8">
<title>Halvor Homeworks – Van Side Wrap</title>
<link rel="stylesheet" href="https://fonts.googleapis.com/css2?family=Oswald:wght@500;600&family=Poppins:wght@500;600&display=swap">
<style>
  :root{
    --bg:#eef0f2;
    --wrap-white:#ffffff;
    --wrap-grey:#e4e6e9;
    --ink:#1c1c1e;
    --purple:#7a2a8c;
    --purple-dark:#5e1f6d;
    --wood:#9a6b44;
    --cabinet:#f2f2f0;
    --island:#222226;
  }
  *{box-sizing:border-box;margin:0;padding:0}
  html,body{width:1200px;height:1200px;overflow:hidden;background:var(--bg)}
  .canvas{position:relative;width:1200px;height:1200px}
  .wrap-panel{
    position:absolute;left:50px;width:1100px;height:500px;
    background:linear-gradient(180deg,var(--wrap-white) 0%,var(--wrap-white) 70%,var(--wrap-grey) 100%);
    border-radius:18px;overflow:hidden;
    box-shadow:0 2px 10px rgba(0,0,0,.08);
  }
  .wrap-panel--clean{top:60px}
  .wrap-panel--sketch{top:640px}
  .sketch-area{
    position:absolute;left:300px;top:0;width:480px;height:380px;
    background:linear-gradient(135deg,rgba(120,120,130,.10),rgba(255,255,255,0) 55%,rgba(120,120,130,.12));
  }
  .kitchen-photo{
    position:absolute;right:0;top:0;width:400px;height:380px;
    background:
      linear-gradient(180deg,var(--cabinet) 0%,#dcdcdc 45%,transparent 45%),
      linear-gradient(90deg,var(--wood) 0%,#b4865b 40%,var(--island) 40%,var(--island) 100%);
  }
  .page-curl{position:absolute;left:640px;top:0;width:160px;height:380px}
  .brand-name{
    position:absolute;left:320px;top:78px;width:330px;
    font-family:'Oswald',sans-serif;font-weight:600;font-size:54px;
    letter-spacing:3px;color:var(--ink);line-height:1.05;text-align:center;
  }
  .services{
    position:absolute;left:320px;top:250px;width:330px;
    font-family:'Oswald',sans-serif;font-weight:600;font-size:15px;
    color:var(--ink);line-height:1.4;text-align:center;white-space:nowrap;
  }
  .services .sep{color:var(--purple)}
  .contact{position:absolute;left:120px;top:250px}
  .contact-phone{
    font-family:'Poppins',sans-serif;font-weight:600;font-size:20px;
    letter-spacing:4px;color:var(--ink);line-height:1.2;
  }
  .contact-web{
    font-family:'Poppins',sans-serif;font-weight:500;font-size:10.5px;color:var(--purple);
  }
  .address-band{
    position:absolute;left:110px;right:0;top:392px;height:46px;
    background:linear-gradient(180deg,var(--purple) 0%,var(--purple-dark) 100%);
    display:flex;align-items:center;padding-left:200px;
  }
  .address-band span{
    font-family:'Poppins',sans-serif;font-weight:600;font-size:17px;
    letter-spacing:2.5px;color:#fff;white-space:nowrap;
  }
  .rocker{position:absolute;left:0;right:0;top:438px;height:62px;background:#2a2a2c}
</style>
</head>
<body>
<main class="canvas">

  <section class="wrap-panel wrap-panel--clean">
    <div class="kitchen-photo" role="img" aria-label="Photo of a modern white kitchen with dark island, bar stools and wood floor"></div>
    <svg class="page-curl" viewBox="0 0 160 380" aria-hidden="true">
      <defs>
        <linearGradient id="curlA" x1="0" x2="1"><stop offset="0" stop-color="#ffffff"/><stop offset=".7" stop-color="#d4d6d9"/><stop offset="1" stop-color="#a9acb0"/></linearGradient>
      </defs>
      <path d="M60 0 C40 60 80 110 50 170 C20 230 70 300 30 380 L0 380 L0 0 Z" fill="#ffffff"/>
      <path d="M60 0 C40 60 80 110 50 170 C20 230 70 300 30 380 L90 380 C120 300 70 230 100 170 C130 110 90 60 110 0 Z" fill="url(#curlA)"/>
    </svg>
    <div class="brand-name">HALVOR<br>HOMEWORKS</div>
    <div class="contact">
      <div class="contact-phone">301.555.0148</div>
      <div class="contact-web">www.halvorhomeworks.example</div>
    </div>
    <div class="services">
      HOME IMPROVEMENT <span class="sep">|</span> KITCHEN AND BATH REMODELING<br>
      HOME ADDITIONS <span class="sep">|</span> SUNROOM <span class="sep">|</span> DECK <span class="sep">|</span> PATIO <span class="sep">|</span> PORCH
    </div>
    <div class="address-band"><span>4817 Halberd Ave Silver Spring MD 20910</span></div>
    <div class="rocker"></div>
  </section>

  <section class="wrap-panel wrap-panel--sketch">
    <div class="sketch-area" role="img" aria-label="Faint line sketch of a kitchen layout fading into the white side"></div>
    <div class="kitchen-photo" role="img" aria-label="Photo of a modern white kitchen with dark island, bar stools and wood floor"></div>
    <svg class="page-curl" viewBox="0 0 160 380" aria-hidden="true">
      <defs>
        <linearGradient id="curlB" x1="0" x2="1"><stop offset="0" stop-color="#ffffff"/><stop offset=".7" stop-color="#d4d6d9"/><stop offset="1" stop-color="#a9acb0"/></linearGradient>
      </defs>
      <path d="M60 0 C40 60 80 110 50 170 C20 230 70 300 30 380 L90 380 C120 300 70 230 100 170 C130 110 90 60 110 0 Z" fill="url(#curlB)"/>
    </svg>
    <div class="brand-name">HALVOR<br>HOMEWORKS</div>
    <div class="contact">
      <div class="contact-phone">301.555.0148</div>
      <div class="contact-web">www.halvorhomeworks.example</div>
    </div>
    <div class="services">
      HOME IMPROVEMENT <span class="sep">|</span> KITCHEN AND BATH REMODELING<br>
      HOME ADDITIONS <span class="sep">|</span> SUNROOM <span class="sep">|</span> DECK <span class="sep">|</span> PATIO <span class="sep">|</span> PORCH
    </div>
    <div class="address-band"><span>4817 Halberd Ave Silver Spring MD 20910</span></div>
    <div class="rocker"></div>
  </section>

</main>
</body>
</html>
```